Live Scavenger Hunt Mobile Platform needs a face lift!

We have been live for the past year and serving some very large customers, however, we are a group of developers that lack any real design skills. We are looking for a designer to help take our apps look and feel to the next level.

You can see the app in the Quellmart store here: https://apps.quellmart.example/us/app/trovanta.app/id913582047?mt=8

And in brindle pix here: https://shop.brindlepix.example/store/apps/developer?id=trovantaapp&hl=en

We do not plan to change the UX of app, but rather just the aesthetics. Ideally, if this project works out well we would work with the same designer to update our site: http://trovanta.app

You can watch a video of how the platform works here:
http://clipsharva.example/user8831054/elf-themed-christmas-scavenger-hunt

I have included the PSD files we used for the current mobile apps along with the PSD for our logo. In terms of colors we do like the current green and orange/red found in the logo. We have started to gravitate towards a brown textured background, but am open to change on this.

Industry/Entity Type

Store

Requirements
Must have
• The home screen should have a larger focus on getting started vs. the other three categories of 'hunts, settings and help'. We worked with a Marlowbrook designer when re-skinning the app for the experience an we liked how they did this.

https://apps.quellmart.example/us/app/pantry-quest/id730418855?mt=8
Nice to have
• - Custom web font (Some what playful) I am using Hobo Std in our logo
- Textured background
- Fun and playful, yet clean and clear. (Yes I realize that is a challenge)

```html
<!DOCTYPE html>
<html lang="en">
<head>
<meta charset="utf-8">
<title>Trovanta – Challenges</title>
<link href="https://fonts.googleapis.com/css2?family=PT+Sans:wght@400;700&display=swap" rel="stylesheet">
<style>
  :root {
    --header-top: #35322f;
    --header-bottom: #1c1b1a;
    --white: #ffffff;
    --tab-active: #4f9c10;
    --tab-idle: #e1f3c6;
    --tab-idle-text: #2f4a1c;
    --item-top: #ffffff;
    --item-bottom: #ebe9ea;
    --item-divider: #d4d2d3;
    --title: #26351c;
    --meta: #4e4e4e;
    --chevron: #cfcfcf;
    --bar-green: #5ab52a;
    --bar-light: #8fd65a;
    --panel: #272727;
    --table: #2e2e2e;
    --table-line: #3d3d3d;
    --label: #868686;
    --tab-dark: #232323;
  }
  * { box-sizing: border-box; margin: 0; padding: 0; }
  html, body { width: 800px; height: 1200px; overflow: hidden; }
  body { font-family: "PT Sans", sans-serif; background: var(--panel); position: relative; }

  .app-header {
    position: absolute; left: 0; top: 0; width: 800px; height: 109px;
    background: linear-gradient(var(--header-top), var(--header-bottom));
    display: flex; align-items: center; justify-content: center;
  }
  .back-button { position: absolute; left: 46px; top: 34px; width: 60px; height: 44px; }
  .settings-button { position: absolute; left: 700px; top: 30px; width: 50px; height: 50px; }
  .brand-name { color: var(--white); font-size: 44px; font-weight: 700; letter-spacing: 0.5px; }

  .tabs { position: absolute; left: 0; top: 109px; width: 800px; height: 60px; display: flex; }
  .tab { flex: 0 0 auto; display: flex; align-items: center; justify-content: center; font-size: 23px; }
  .tab--active { width: 398px; background: var(--tab-active); color: var(--white); }
  .tab--idle { width: 402px; background: var(--tab-idle); color: var(--tab-idle-text); }

  .challenge-list { position: absolute; left: 0; top: 169px; width: 800px; }
  .challenge {
    height: 177.5px; margin-bottom: 2.5px; position: relative;
    background: linear-gradient(var(--item-top), var(--item-bottom));
    border-bottom: 1px solid var(--item-divider);
    padding: 63px 0 0 55px;
  }
  .challenge__title { font-size: 30px; font-weight: 700; color: var(--title); line-height: 1; }
  .challenge__points { font-size: 21px; color: var(--meta); margin-top: 10px; line-height: 1; }
  .challenge__chevron { position: absolute; left: 693px; top: 66px; width: 40px; height: 48px; }

  .score-bar {
    position: absolute; left: 0; top: 706px; width: 800px; height: 24px;
    background: linear-gradient(90deg, var(--bar-light) 0, var(--bar-green) 6%, var(--bar-green) 94%, var(--bar-light) 100%);
  }
  .score-tab {
    position: absolute; left: 332px; top: 676px; width: 106px; height: 54px;
    background: var(--tab-dark); border-radius: 8px 8px 0 0;
    color: var(--white); font-size: 22px; display: flex; align-items: center; justify-content: center;
  }

  .score-table {
    position: absolute; left: 28px; top: 880px; width: 750px;
    background: var(--table); border: 1px solid var(--table-line); border-collapse: collapse;
  }
  .score-table td { height: 85px; border-bottom: 1px solid var(--table-line); font-size: 25px; }
  .score-table tr:last-child td { border-bottom: none; }
  .score-table .label { color: var(--label); padding-left: 70px; width: 367px; }
  .score-table .value { color: var(--white); }
</style>
</head>
<body>
  <header class="app-header">
    <svg class="back-button" viewBox="0 0 60 44" aria-label="Back">
      <path d="M0 22 L24 0 V13 H58 V31 H24 V44 Z" fill="#ffffff"/>
    </svg>
    <span class="brand-name">Trovanta</span>
    <svg class="settings-button" viewBox="0 0 50 50" aria-label="Settings">
      <g fill="#ffffff" transform="translate(25 25)">
        <rect x="-5" y="-25" width="10" height="12" rx="2"/>
        <rect x="-5" y="-25" width="10" height="12" rx="2" transform="rotate(45)"/>
        <rect x="-5" y="-25" width="10" height="12" rx="2" transform="rotate(90)"/>
        <rect x="-5" y="-25" width="10" height="12" rx="2" transform="rotate(135)"/>
        <rect x="-5" y="-25" width="10" height="12" rx="2" transform="rotate(180)"/>
        <rect x="-5" y="-25" width="10" height="12" rx="2" transform="rotate(225)"/>
        <rect x="-5" y="-25" width="10" height="12" rx="2" transform="rotate(270)"/>
        <rect x="-5" y="-25" width="10" height="12" rx="2" transform="rotate(315)"/>
        <circle r="17"/>
      </g>
      <circle cx="25" cy="25" r="7.5" fill="#262422"/>
    </svg>
  </header>

  <nav class="tabs">
    <div class="tab tab--active">Challenges</div>
    <div class="tab tab--idle">Completed</div>
  </nav>

  <section class="challenge-list">
    <div class="challenge">
      <div class="challenge__title">Shoe Shine</div>
      <div class="challenge__points">3 points</div>
      <svg class="challenge__chevron" viewBox="0 0 40 48"><path d="M0 0 H16 L40 24 L16 48 H0 L24 24 Z" fill="var(--chevron)"/></svg>
    </div>
    <div class="challenge">
      <div class="challenge__title">Unicorn of the sea</div>
      <div class="challenge__points">3 points</div>
      <svg class="challenge__chevron" viewBox="0 0 40 48"><path d="M0 0 H16 L40 24 L16 48 H0 L24 24 Z" fill="var(--chevron)"/></svg>
    </div>
    <div class="challenge">
      <div class="challenge__title">Reindeer</div>
      <div class="challenge__points">3 points</div>
      <svg class="challenge__chevron" viewBox="0 0 40 48"><path d="M0 0 H16 L40 24 L16 48 H0 L24 24 Z" fill="var(--chevron)"/></svg>
    </div>
  </section>

  <div class="score-bar"></div>
  <div class="score-tab">Score</div>

  <table class="score-table">
    <tr><td class="label">Your Score:</td><td class="value">2 points</td></tr>
    <tr><td class="label">Time left:</td><td class="value">58 minutes</td></tr>
    <tr><td class="label">Challenges</td><td class="value">1 of 30</td></tr>
  </table>
</body>
</html>
```